Kestrelwood Restaurnt Lunch Menu Redesign:

We have two lunch special menus that need to be reformatted into a 4.25inx11in and need a graphics design update. Some menu items need to change and some descriptions need to updated. This new menu should double sided with the Main Dining Lunch Menu on the front side and Teppanyaki Lunch menu on the back.

Both menus should follow the same design formatting as the main dining lunch menu (font, sizing, ect.)

```html
<!DOCTYPE html>
<html lang="en">
<head>
<meta charset="utf-8">
<title>Kestrelwood Restaurnt — Lunch Menus</title>
<link href="https://fonts.googleapis.com/css2?family=Gloock&family=Allura&family=Poppins:wght@400;500;600;700&family=Libre+Caslon+Text&display=swap" rel="stylesheet">
<style>
  :root{
    --blue:#1f4594;
    --band:#1c3f8c;
    --ink:#1b1b22;
    --muted:#3a3a44;
    --rule:#9aa6c4;
    --paper:#ffffff;
    --wave-a:#ffffff;
    --wave-b:#eef0f5;
    --stage:#ececec;
  }
  *{margin:0;padding:0;box-sizing:border-box}
  html,body{width:1200px;height:1198px;overflow:hidden;background:var(--stage)}
  body{position:relative;font-family:"Poppins",sans-serif;color:var(--ink)}

  .menu-card{position:absolute;top:124px;height:950px;background:var(--paper);overflow:hidden}
  .menu-card--dining{left:174px;width:352px}
  .menu-card--teppanyaki{left:642px;width:368px}

  .wave-texture{position:absolute;inset:0;background:radial-gradient(circle at 50% 40%,var(--wave-a) 0%,var(--wave-b) 100%)}
  .card-body{position:absolute;inset:0}

  .title{position:absolute;left:0;right:0;text-align:center;font-family:"Gloock",serif;color:var(--blue);line-height:1}
  .script{position:absolute;left:0;right:0;text-align:center;font-family:"Allura",cursive;color:var(--ink);line-height:1}
  .rule{position:absolute;left:36px;right:36px;height:1px;background:var(--rule)}
  .hours{position:absolute;left:0;right:0;text-align:center;font-weight:600;color:var(--blue);font-size:14.5px}
  .hours span{margin-left:14px}

  .section-head{position:absolute;left:30px;font-family:"Gloock",serif;color:var(--blue);font-size:17px;letter-spacing:.2px}
  .note-box{position:absolute;left:30px;right:18px;border:1px solid var(--rule);background:#fff;padding:4px 8px;font-size:9.6px;line-height:1.3;color:var(--ink)}
  .note-box sup,.price sup{font-size:.6em;vertical-align:top;position:relative;top:-1px}
  .note-box .price-inline{font-family:"Libre Caslon Text",serif;color:var(--blue);margin-left:14px}

  .item-list{position:absolute;left:30px;right:24px;list-style:none}
  .item{position:relative;padding-right:30px}
  .item-name{font-weight:600;font-size:10px;line-height:1.3}
  .item-desc{font-size:9.6px;line-height:1.3;color:var(--muted)}
  .item-desc--small{font-size:8px}
  .price{position:absolute;right:0;top:0;font-family:"Libre Caslon Text",serif;color:var(--blue);font-size:10px}

  .sandwich-list .item{margin-bottom:6px}
  .main-list .item{margin-bottom:3px}

  .sushi-grid{position:absolute;left:30px;right:24px;display:grid;grid-template-columns:1fr 1fr;column-gap:10px;font-size:9.6px;line-height:14.4px}
  .sushi-grid b{font-weight:600}
  .sushi-grid ul{list-style:none}

  .legal-band{position:absolute;left:0;right:0;bottom:0;height:57px;background:var(--band);color:#fff;font-size:7.4px;line-height:1.25;padding:10px 30px 0}

  .price-list{position:absolute;list-style:none}
  .price-row{display:flex;align-items:baseline;height:21.6px;font-size:9.8px;font-weight:600}
  .price-row .leader{flex:1;border-bottom:1px dotted #c9cdd8;margin:0 8px;transform:translateY(-3px)}
  .price-row .price{position:static;font-size:10.5px}

  .special-frame{position:absolute;left:33px;width:303px;top:548px;height:324px;border:1px solid var(--blue);background:#fff}
  .sparkle{position:absolute;top:14px;width:10px;height:10px}

  .contact-band{position:absolute;left:0;right:0;bottom:0;height:57px;background:var(--band);color:#fff;display:flex;align-items:center;justify-content:center;font-size:10px;font-weight:500;gap:14px}
  .contact-band .divider{width:1px;height:20px;background:rgba(255,255,255,.6)}
  .contact-item{display:flex;align-items:center;gap:6px}
</style>
</head>
<body>

<!-- Main dining lunch menu -->
<section class="menu-card menu-card--dining" aria-label="Kestrelwood Restaurnt lunch specials">
  <div class="wave-texture" role="img" aria-label="Subtle seigaiha wave pattern background"></div>
  <div class="card-body">
    <h1 class="title" style="top:30px;font-size:50px;letter-spacing:2px">LUNCH</h1>
    <p class="script" style="top:80px;font-size:36px">Specials</p>
    <div class="rule" style="top:131px"></div>
    <p class="hours" style="top:148px">Served Daily <span>11AM - 3PM</span></p>
    <div class="rule" style="top:170px"></div>

    <h2 class="section-head" style="top:198px">SANDWICHES</h2>
    <div class="note-box" style="top:218px">Served with Choice of Miso Soup or House Salad<br>&amp; Potato Chips</div>
    <ul class="item-list sandwich-list" style="top:262px">
      <li class="item"><div class="item-name">Fried Breaded Calamari Steak</div><div class="item-desc">With Tomato, Lettuce &amp; Onion</div><span class="price"><sup>$</sup>16</span></li>
      <li class="item"><div class="item-name">Grilled Chicken</div><div class="item-desc">With Bacon, Tomato, Lettuce &amp; Mayonnaise Drizzle</div><span class="price"><sup>$</sup>16</span></li>
      <li class="item"><div class="item-name">Hamburger</div><div class="item-desc">With Lettuce, Tomato, Onion, Mayonnaise Drizzle</div><span class="price"><sup>$</sup>18</span></li>
      <li class="item"><div class="item-name">Fried Soft Shell Crab Burger</div><div class="item-desc">With Avocado, Lettuce, Tomato, Onion &amp; Mayo</div><span class="price"><sup>$</sup>20</span></li>
    </ul>

    <h2 class="section-head" style="top:410px">SUSHI SPECIALS</h2>
    <div class="note-box" style="top:430px">Please Select 4 of the followings for <span class="price-inline"><sup>$</sup>16</span><br>Served with a 4 piece California Roll &amp; Miso Soup<br>or House Salad</div>
    <div class="sushi-grid" style="top:490px">
      <ul>
        <li><b>Hamachi</b> - Yellowtail Tuna</li>
        <li><b>Hotate</b> - Scallop</li>
        <li><b>Ika</b> - Squid</li>
        <li><b>Ikura</b> - Salmon Roe</li>
        <li><b>Saba</b> - Mackerel</li>
        <li><b>Sake</b> - Salmon</li>
        <li><b>Tai</b> - Red Snapper</li>
      </ul>
      <ul>
        <li><b>Maguro</b> - Yellow fin Tuna</li>
        <li><b>Smoked Salmon</b></li>
        <li>&nbsp;</li>
        <li><b>Tako</b> - Octopus</li>
        <li><b>Unagi</b> - BBQ Eel</li>
        <li><b>Ebi</b> - Shrimp</li>
        <li><b>Tamago</b> - Egg</li>
      </ul>
    </div>

    <h2 class="section-head" style="top:616px">MAIN COURSES</h2>
    <div class="note-box" style="top:640px">Served with Rice &amp; Choice of Miso Soup or House Salad<br>All Meals Served with Rice. Upgrade to fried rice for only <sup>$</sup>4</div>
    <ul class="item-list main-list" style="top:688px">
      <li class="item"><div class="item-name">Organic Tofu Teriyaki</div><div class="item-desc">Served Grilled or Tempura Fried</div><span class="price"><sup>$</sup>14</span></li>
      <li class="item"><div class="item-name">Chicken Teriyaki</div><span class="price"><sup>$</sup>16</span></li>
      <li class="item"><div class="item-name">Spicy Chicken Teriyaki</div><span class="price"><sup>$</sup>16</span></li>
      <li class="item"><div class="item-name">Beef Teriyaki</div><span class="price"><sup>$</sup>16</span></li>
      <li class="item"><div class="item-name">Spicy Beef Teriyaki</div><span class="price"><sup>$</sup>16</span></li>
      <li class="item"><div class="item-name">Chicken Katsu</div><div class="item-desc">Breaded Chicken Breast</div><span class="price"><sup>$</sup>15</span></li>
      <li class="item"><div class="item-name">Katsu Don</div><div class="item-desc item-desc--small">Fried Chicken Breast, Egg &amp; Onion over Rice</div><span class="price"><sup>$</sup>16</span></li>
      <li class="item"><div class="item-name">Unagi Don</div><div class="item-desc">BBQ Eel over Rice</div><span class="price"><sup>$</sup>19</span></li>
      <li class="item"><div class="item-name">Shrimp &amp; Vegetable Tempura</div><span class="price"><sup>$</sup>16</span></li>
    </ul>

    <footer class="legal-band">
      Served Raw<br>
      20% gratuity added to parties of 6 or more.<br>
      Consuming raw or undercooked food may increase your risk of foodborne illness
    </footer>
  </div>
</section>

<!-- Teppanyaki lunch menu -->
<section class="menu-card menu-card--teppanyaki" aria-label="Kestrelwood Restaurnt teppanyaki lunch">
  <div class="wave-texture" role="img" aria-label="Subtle seigaiha wave pattern background"></div>
  <div class="card-body">
    <h1 class="title" style="top:40px;font-size:37px;letter-spacing:3px">TEPPANYAKI</h1>
    <p class="script" style="top:82px;font-size:38px">Lunch</p>
    <div class="rule" style="top:126px"></div>
    <p class="hours" style="top:133px">Available until 11-2:30pm</p>
    <div class="rule" style="top:158px"></div>
    <div class="note-box" style="top:164px;left:33px;right:33px;text-align:center">Served with Miso Soup or Salad, Choice of Rice &amp; Vegetables</div>

    <ul class="price-list" style="top:205px;left:31px;right:31px">
      <li class="price-row">Hibachi Chicken<span class="leader"></span><span class="price"><sup>$</sup>18.00</span></li>
      <li class="price-row">Hibachi Shrimp<span class="leader"></span><span class="price"><sup>$</sup>19.00</span></li>
      <li class="price-row">Hibachi New York Steak<span class="leader"></span><span class="price"><sup>$</sup>20.00</span></li>
      <li class="price-row">Hibachi Salmon<span class="leader"></span><span class="price"><sup>$</sup>20.00</span></li>
      <li class="price-row">Teriyaki Beef<span class="leader"></span><span class="price"><sup>$</sup>19.00</span></li>
      <li class="price-row">Hibachi Scallop<span class="leader"></span><span class="price"><sup>$</sup>20.00</span></li>
      <li class="price-row">Chicken and Shrimp<span class="leader"></span><span class="price"><sup>$</sup>21.00</span></li>
      <li class="price-row">Scallop and Shrimp<span class="leader"></span><span class="price"><sup>$</sup>22.00</span></li>
      <li class="price-row">New York Steak and Chicken<span class="leader"></span><span class="price"><sup>$</sup>22.00</span></li>
      <li class="price-row">New York Steak and Shrimp<span class="leader"></span><span class="price"><sup>$</sup>23.00</span></li>
      <li class="price-row">New York Steak and Scallop<span class="leader"></span><span class="price"><sup>$</sup>24.00</span></li>
      <li class="price-row">Filet Mignon<span class="leader"></span><span class="price"><sup>$</sup>23.00</span></li>
      <li class="price-row">Filet Mignon and Chicken<span class="leader"></span><span class="price"><sup>$</sup>25.00</span></li>
      <li class="price-row">Filet Mignon and Shrimp<span class="leader"></span><span class="price"><sup>$</sup>26.00</span></li>
      <li class="price-row">Filet Mignon and Scallop<span class="leader"></span><span class="price"><sup>$</sup>27.00</span></li>
    </ul>

    <div class="special-frame">
      <svg class="sparkle" style="left:34px" viewBox="0 0 10 10" aria-hidden="true"><path d="M5 0 L6 4 L10 5 L6 6 L5 10 L4 6 L0 5 L4 4 Z" fill="var(--blue)"/></svg>
      <svg class="sparkle" style="right:34px" viewBox="0 0 10 10" aria-hidden="true"><path d="M5 0 L6 4 L10 5 L6 6 L5 10 L4 6 L0 5 L4 4 Z" fill="var(--blue)"/></svg>
      <h2 class="title" style="top:30px;font-size:38px;letter-spacing:3px">SPECIAL</h2>
      <p class="script" style="top:72px;font-size:36px">Menu</p>
      <div class="note-box" style="top:124px;left:18px;right:18px;text-align:center;font-size:9.4px">
        <strong style="font-weight:600">Ages 12 and Under ~ Ages 65 and Older</strong><br>
        Served with Miso Soup or Salad, Choice of<br>Rice &amp; Vegetables
      </div>
      <ul class="price-list" style="top:181px;left:14px;right:14px">
        <li class="price-row">Hibachi Chicken<span class="leader"></span><span class="price"><sup>$</sup>15.00</span></li>
        <li class="price-row">Hibachi Shrimp<span class="leader"></span><span class="price"><sup>$</sup>16.00</span></li>
        <li class="price-row">Hibachi Scallop<span class="leader"></span><span class="price"><sup>$</sup>18.00</span></li>
        <li class="price-row">Hibachi New York Steak<span class="leader"></span><span class="price"><sup>$</sup>18.00</span></li>
        <li class="price-row">Hibachi Scallop<span class="leader"></span><span class="price"><sup>$</sup>18.00</span></li>
        <li class="price-row">Teriyaki Beef<span class="leader"></span><span class="price"><sup>$</sup>16.00</span></li>
      </ul>
    </div>

    <footer class="contact-band">
      <span class="contact-item">
        <svg width="12" height="12" viewBox="0 0 24 24" aria-hidden="true"><circle cx="12" cy="12" r="12" fill="#fff"/><path d="M8.2 6.5c.4-.3 1-.3 1.3.1l1.3 1.8c.3.4.2.9-.1 1.2l-.8.7c.6 1.3 1.6 2.4 2.9 3l.7-.8c.3-.3.8-.4 1.2-.1l1.8 1.3c.4.3.5.9.1 1.3l-.9 1c-.5.5-1.3.7-2 .4-3-1.2-5.4-3.6-6.5-6.6-.3-.7-.1-1.5.4-2z" fill="var(--band)"/></svg>
        +1 707-555-0148
      </span>
      <span class="divider"></span>
      <span class="contact-item">
        <svg width="11" height="11" viewBox="0 0 10 10" aria-hidden="true"><circle cx="5" cy="5" r="5" fill="#fff"/></svg>
        @kestrelwoodeureka
      </span>
    </footer>
  </div>
</section>

</body>
</html>
```